In Search of a FANTASTIC BUSINESS CARD REFRESH AND REDESIGN

I would like to redesign the current business card for my company.  There is a parent company, Brenford Care Group, with 2 operating companies - Brenford Homecare and Brenford Senior Living.
I will include the current business card design, along with the 3 logos I would like incorporated.  The business card can be two sided.  I'm looking for something clean, professional, and a fresh new look.

Target Market(s)
Hospitals, social workers, insurance agents, family members of seniors
Industry/Entity Type
Healthcare
Contact Information for Business Card
Name, title of person, address, phone number, web address, email address
Look and feel
Each slider illustrates characteristics of the customer's brand and the style your logo design should communicate.

```html
<!DOCTYPE html>
<html lang="en">
<head>
<meta charset="utf-8">
<title>Brenford Care Group – Business Card</title>
<link href="https://fonts.googleapis.com/css2?family=Lora:ital,wght@0,500;1,400&family=Roboto:wght@400;500;700&display=swap" rel="stylesheet">
<style>
  :root {
    --bg: #e9e7e4;
    --teal: #569592;
    --pink: #f28b8b;
    --grey: #6b6b6b;
    --ink: #4a4a4a;
    --white: #ffffff;
  }
  * { margin: 0; padding: 0; box-sizing: border-box; }
  html, body { width: 1200px; height: 912px; overflow: hidden; background: var(--bg); }
  body { position: relative; font-family: "Roboto", Arial, sans-serif; }

  .card {
    position: absolute;
    width: 620px;
    height: 354px;
    box-shadow: 0 10px 28px rgba(0,0,0,.18);
    overflow: hidden;
  }

  /* Back: parent company */
  .card-back { left: 60px; top: 60px; background: var(--teal); }
  .parent-brand {
    position: absolute; left: 0; right: 0; top: 112px;
    display: flex; align-items: center; justify-content: center; gap: 14px;
  }
  .brand-square { width: 34px; height: 34px; border-radius: 6px; flex: none; }
  .parent-brand .brand-square { background: var(--white); }
  .brand-name { font-family: "Lora", Georgia, serif; font-weight: 500; white-space: nowrap; }
  .parent-brand .brand-name { color: var(--white); font-size: 38px; }
  .tagline {
    position: absolute; left: 0; right: 0; top: 180px;
    text-align: center; color: var(--white);
    font-family: "Lora", Georgia, serif; font-style: italic; font-size: 16px; line-height: 1.35;
  }

  /* Front: contact side */
  .card-front { left: 520px; top: 490px; background: var(--white); }
  .homecare-brand {
    position: absolute; left: 34px; top: 40px;
    display: flex; align-items: center; gap: 10px;
  }
  .homecare-brand .brand-square { background: var(--pink); width: 28px; height: 28px; }
  .homecare-brand .brand-name { color: var(--grey); font-size: 26px; }

  .senior-brand {
    position: absolute; right: 34px; top: 40px;
    display: flex; align-items: center; gap: 10px;
  }
  .senior-brand .brand-square { background: var(--teal); width: 24px; height: 24px; }
  .senior-brand .brand-name { color: var(--teal); font-size: 19px; }

  .person { position: absolute; left: 34px; top: 138px; }
  .person-name { font-weight: 700; font-size: 22px; letter-spacing: .3px; }
  .person-name .first { color: var(--teal); }
  .person-name .last { color: var(--pink); }
  .person-title { color: var(--grey); font-size: 15px; margin-top: 2px; }

  .divider { position: absolute; height: 1.5px; background: var(--pink); }
  .divider-main { left: 34px; right: 40px; top: 206px; }

  .contact-list { position: absolute; left: 34px; top: 220px; list-style: none; }
  .contact-list li {
    display: flex; align-items: center; gap: 8px;
    color: var(--ink); font-size: 15px; line-height: 20px;
  }
  .contact-list svg { width: 12px; height: 12px; flex: none; }

  .address {
    position: absolute; right: 40px; top: 222px; text-align: right;
    color: var(--ink); font-size: 14px; line-height: 18px;
  }

  .footer-band { position: absolute; left: 0; bottom: 0; width: 620px; height: 80px; }
  .web {
    position: absolute; right: 30px; bottom: 14px;
    color: var(--white); font-weight: 500; font-size: 15px; letter-spacing: 1.5px;
  }
</style>
</head>
<body>

<section class="card card-back" aria-label="Business card back">
  <div class="parent-brand">
    <span class="brand-square"></span>
    <span class="brand-name">Brenford Care Group</span>
  </div>
  <p class="tagline">Care you can count on...<br>Every single day.</p>
</section>

<section class="card card-front" aria-label="Business card front">
  <div class="homecare-brand">
    <span class="brand-square"></span>
    <span class="brand-name">Brenford Homecare</span>
  </div>
  <div class="senior-brand">
    <span class="brand-square"></span>
    <span class="brand-name">Brenford Senior Living</span>
  </div>

  <div class="person">
    <p class="person-name"><span class="first">MARLA</span> <span class="last">BRENFORD</span></p>
    <p class="person-title">President, CEO</p>
  </div>

  <div class="divider divider-main"></div>

  <ul class="contact-list">
    <li>
      <svg viewBox="0 0 12 12" aria-hidden="true"><path d="M2.5 1l2 2-1 1.3c.6 1.3 1.6 2.3 2.9 2.9L7.7 6.2l2 2-1.2 1.6C5 9.6 2.2 6.8 1 3.3z" fill="var(--teal)"/></svg>
      (808) 555-0142
    </li>
    <li>
      <svg viewBox="0 0 12 12" aria-hidden="true"><rect x="3" y="1" width="6" height="3" fill="none" stroke="var(--teal)"/><rect x="1" y="4" width="10" height="5" rx="1" fill="none" stroke="var(--teal)"/><rect x="3" y="7" width="6" height="4" fill="var(--white)" stroke="var(--teal)"/></svg>
      (808) 555-0187
    </li>
    <li>
      <svg viewBox="0 0 12 12" aria-hidden="true"><rect x="1" y="2.5" width="10" height="7" fill="none" stroke="var(--teal)"/><path d="M1 2.5l5 4 5-4" fill="none" stroke="var(--teal)"/></svg>
      marla@brenfordcare.com
    </li>
  </ul>

  <p class="address">4870 makani street, suite<br>210, honolulu, hi 96815</p>

  <svg class="footer-band" viewBox="0 0 620 80" preserveAspectRatio="none" aria-hidden="true">
    <path d="M0 56 L360 56 L350 62 L0 62 Z" fill="var(--pink)"/>
    <path d="M0 68 L370 68 C400 68 410 30 450 30 L620 30 L620 80 L0 80 Z" fill="var(--teal)"/>
  </svg>
  <p class="web">www.brenfordcare.com</p>
</section>

</body>
</html>
```